We need a flyer design for a new program aimed at getting young kids into cricket. The information provided with the design is to inform parents of a discount on membership to join these programs. The program is called Pass4Wicket and the logos provided have been approved to use as well as 2 photos from bowling Marlowe to use if needed. Format needs to have Z40 surge and vanta go4bowling at top with the Pass4Wicket wording in any format you design. The Ferrowind city council bottom left and bowling Marlowe bottom right. With text (example shown) in the middle.

```html
<!DOCTYPE html>
<html lang="en">
<head>
<meta charset="utf-8">
<title>Pass4Wicket Flyer</title>
<link rel="stylesheet" href="https://fonts.googleapis.com/css2?family=Cormorant+Garamond:wght@600&family=Roboto+Condensed:wght@300;400;700&display=swap">
<style>
  :root {
    --backdrop: #2e2925;
    --flyer-green: #3f7a43;
    --flyer-green-dark: #2c5a32;
    --band-paper: #eeece5;
    --band-edge: #ffffff;
    --title-green: #3e6146;
    --text-white: #ffffff;
    --text-soft: #dbe7d6;
    --photo-top: #4b8a3e;
    --photo-bottom: #1f3d22;
  }
  * { margin: 0; padding: 0; box-sizing: border-box; }
  html, body { width: 1200px; height: 1000px; overflow: hidden; background: var(--backdrop); }
  .flyer {
    position: absolute; left: 285px; top: 48px; width: 630px; height: 887px;
    background: radial-gradient(ellipse at 55% 45%, var(--flyer-green) 0%, var(--flyer-green-dark) 100%);
    font-family: "Roboto Condensed", sans-serif; color: var(--text-white);
    overflow: hidden;
  }
  .program-marks { position: absolute; top: 48px; left: 0; width: 100%; display: flex; justify-content: center; gap: 16px; z-index: 2; }
  .program-mark { display: flex; align-items: center; gap: 6px; font-weight: 700; font-size: 15px; color: var(--text-white); }
  .program-mark .dot { width: 12px; height: 12px; border-radius: 50%; background: var(--text-white); }
  .title-band {
    position: absolute; top: 100px; left: 0; width: 100%; height: 144px;
    background: var(--band-paper);
    border-top: 4px solid var(--band-edge); border-bottom: 4px solid var(--band-edge);
    text-align: center;
  }
  .title-band h1 {
    font-family: "Cormorant Garamond", serif; font-weight: 600; font-size: 84px;
    color: var(--title-green); line-height: 1; margin-top: 30px; letter-spacing: 1px;
  }
  .title-band .open-notice {
    font-weight: 300; font-size: 17px; color: var(--title-green);
    text-transform: uppercase; letter-spacing: 1px; margin-top: 2px;
  }
  .headline { position: absolute; top: 278px; left: 30px; right: 30px; text-align: center; font-size: 20px; font-weight: 400; line-height: 1.3; }
  .intro { position: absolute; top: 343px; left: 95px; right: 95px; text-align: center; font-size: 12.5px; font-weight: 300; line-height: 1.3; color: var(--text-soft); }
  .player-photo { position: absolute; left: 105px; top: 425px; width: 210px; height: 462px; }
  .details { position: absolute; left: 333px; top: 445px; width: 255px; font-size: 12.5px; font-weight: 300; line-height: 1.3; color: var(--text-soft); }
  .details h2 { font-size: 17px; font-weight: 700; color: var(--text-white); line-height: 1.2; }
  .details p { margin-bottom: 12px; }
  .details h2 + p { margin-top: 1px; }
  .partner { position: absolute; bottom: 34px; display: flex; align-items: center; gap: 5px; font-size: 10px; font-weight: 700; color: var(--text-white); width: 80px; line-height: 1.1; }
  .partner .square { flex: none; width: 16px; height: 16px; background: var(--text-white); }
  .partner-council { left: 30px; }
  .partner-state { right: 30px; }
</style>
</head>
<body>
  <main class="flyer">
    <div class="program-marks">
      <div class="program-mark"><span class="dot"></span>vanta go4bowling</div>
      <div class="program-mark">Z40 surge</div>
    </div>

    <header class="title-band">
      <h1>Pass4Wicket</h1>
      <p class="open-notice">Applications for 2014/15 Pass4Wicket program are now open</p>
    </header>

    <p class="headline">You could be eligible for 75% off the membership fees up to $100 to join a Vanta go4bowling or Z40 surge program at your local cricket club!</p>

    <p class="intro">Pass4Wicket provides an opportunity for children living in the City of Ferrowind to actively participate in community sport and recreation, regardless of their financial circumstances. Elibible participants can apply for up to $100 financial assistance to contribute to their cricket program membership fees.</p>

    <svg class="player-photo" role="img" aria-label="Photo of a young cricketer in a green kit bowling a red ball" viewBox="0 0 210 462" preserveAspectRatio="none">
      <defs>
        <linearGradient id="player-tone" x1="0" y1="0" x2="0" y2="1">
          <stop offset="0" stop-color="var(--photo-top)"/>
          <stop offset="1" stop-color="var(--photo-bottom)"/>
        </linearGradient>
      </defs>
      <rect width="210" height="462" fill="url(#player-tone)"/>
    </svg>

    <section class="details">
      <h2>Who is Eligible?</h2>
      <p>Applicants must be aged 5-12 years.</p>
      <p>Applicants family must have a Health Care Card or Pension Concession Card.</p>
      <h2>How do I Get Involved?</h2>
      <p>Applicants complete the application form and submit it to their local cricket club to be validated. Applicants must attach a copy of their family's Health Care Card or Pension Card.</p>
      <p>Club validates the application form and returns the form to the applicant.</p>
      <p>Applicant submits the application form to the club upon joining and pays the difference in program membership fees.</p>
      <p>The club invoices Council for up to 75% of membership costs, with a maximum of $100 per child</p>
    </section>

    <div class="partner partner-council"><span class="square"></span>Ferrowind city council</div>
    <div class="partner partner-state"><span class="square"></span>bowling Marlowe</div>
  </main>
</body>
</html>
```